Business Card and Stationary design for new logo
Bright Harbour Makeovers
Professional
Tessa Whitlock & Lewis Whitlock
Director
42 Quenby Crescent
Kestrel Vale NSW 2188
brightharbourmakeovers@fernpost.example
ABN:284 907 362
Color combinations need to remain within company palette of ORANGE, TAN, BLACK AND WHITE. Would prefer ORANGE as main background color for business card design and therefore will need to invert actual logo colors to be able to see all of the design. Would prefer BLACK as the main background color for stationary design as currently have templates where the logo would need to be inserted however would be interested in seeing other designs to make final decision.

```html
<!DOCTYPE html>
<html lang="en">
<head>
<meta charset="utf-8">
<title>Bright Harbour Makeovers – Stationery Set</title>
<link rel="stylesheet" href="https://fonts.googleapis.com/css2?family=Open+Sans:wght@400;700&display=swap">
<style>
  :root{
    --bg:#e9e6e2;
    --paper:#ffffff;
    --ink:#1b1b1b;
    --orange:#e3791c;
    --tan:#f2b262;
    --grey:#8a8a8a;
    --faint:#ececec;
  }
  *{margin:0;padding:0;box-sizing:border-box}
  html,body{width:1200px;height:626px;overflow:hidden;background:var(--bg)}
  body{position:relative;font-family:"Open Sans",Arial,sans-serif;color:var(--ink)}
  .defs{position:absolute;width:0;height:0}
  .sheet{position:absolute;background:var(--paper);overflow:hidden;box-shadow:0 2px 6px rgba(0,0,0,.18)}
  .sheet svg.band{position:absolute;left:0;width:100%}
  .brand{position:absolute;display:flex;align-items:center;gap:5px;z-index:2}
  .brand-dot{border-radius:50%;background:var(--orange);flex:none}
  .brand-name{font-weight:700;color:var(--ink);white-space:nowrap;line-height:1}
  .contact{position:absolute;font-size:4.2px;line-height:1.5;color:#fff;text-align:right;z-index:2}
  .contact.dark{color:var(--ink)}
  .watermark{position:absolute;display:flex;align-items:center;justify-content:center;flex-direction:column;gap:6px}
  .watermark-ring{border-radius:50%;border:10px solid var(--faint)}
  .watermark-name{font-weight:700;color:var(--faint);white-space:nowrap}

  .letterhead-a{left:41px;top:108px;width:302px;height:420px}
  .letterhead-c{left:521px;top:108px;width:300px;height:420px}
  .letterhead-b{left:360px;top:168px;width:293px;height:408px}
  .card-front{left:833px;top:36px;width:151px;height:48px}
  .card-back{left:998px;top:36px;width:144px;height:48px}
  .card-orange{left:912px;top:125px;width:144px;height:67px;background:linear-gradient(100deg,var(--tan),var(--orange) 55%,#7a3a08)}
  .envelope{left:833px;top:240px;width:329px;height:156px}
  .slip{left:833px;top:413px;width:329px;height:163px}
  .card-text{position:absolute;font-size:4.5px;line-height:1.35;color:var(--ink)}
  .card-text strong{color:var(--orange);font-size:5px}
</style>
</head>
<body>

<svg class="defs" aria-hidden="true">
  <defs>
    <linearGradient id="swoosh" x1="0" x2="1" y1="0" y2="0">
      <stop offset="0" stop-color="#f2b262" stop-opacity="0"/>
      <stop offset=".35" stop-color="#f2b262"/>
      <stop offset=".65" stop-color="#e3791c"/>
      <stop offset="1" stop-color="#1b1b1b"/>
    </linearGradient>
    <linearGradient id="swoosh-rev" x1="1" x2="0" y1="0" y2="0">
      <stop offset="0" stop-color="#f2b262" stop-opacity="0"/>
      <stop offset=".35" stop-color="#f2b262"/>
      <stop offset=".65" stop-color="#e3791c"/>
      <stop offset="1" stop-color="#1b1b1b"/>
    </linearGradient>
    <linearGradient id="flap" x1="0" x2="1" y1="0" y2="0">
      <stop offset="0" stop-color="#1b1b1b"/>
      <stop offset=".5" stop-color="#e3791c"/>
      <stop offset="1" stop-color="#1b1b1b"/>
    </linearGradient>
  </defs>
</svg>

<!-- Letterhead with top band -->
<section class="sheet letterhead-a" aria-label="Letterhead, header layout">
  <svg class="band" style="top:0" viewBox="0 0 302 70" height="70" preserveAspectRatio="none">
    <path d="M0 0H302V22C220 14 150 50 0 44Z" fill="url(#swoosh)"/>
    <path d="M0 50C150 56 220 22 302 30" stroke="#1b1b1b" stroke-width="1.4" fill="none"/>
    <path d="M0 55C150 60 220 30 302 36" stroke="#e3791c" stroke-width=".8" fill="none"/>
  </svg>
  <div class="brand" style="left:8px;top:12px"><span class="brand-dot" style="width:12px;height:12px"></span><span class="brand-name" style="font-size:7px">Bright Harbour Makeovers</span></div>
  <div class="contact" style="right:8px;top:4px">42 Quenby Crescent<br>Kestrel Vale NSW 2188<br>brightharbourmakeovers@fernpost.example<br>ABN: 284 907 362</div>
  <div class="watermark" style="left:71px;top:110px" role="img" aria-label="Faint brand mark">
    <span class="watermark-ring" style="width:150px;height:150px"></span>
  </div>
  <svg class="band" style="bottom:0" viewBox="0 0 302 20" height="20" preserveAspectRatio="none">
    <path d="M0 14C100 4 200 20 302 8" stroke="#e3791c" stroke-width="1" fill="none"/>
  </svg>
</section>

<!-- Letterhead with footer band, behind -->
<section class="sheet letterhead-c" aria-label="Letterhead, footer band layout">
  <div class="brand" style="left:8px;top:12px"><span class="brand-dot" style="width:12px;height:12px"></span><span class="brand-name" style="font-size:7px">Bright Harbour Makeovers</span></div>
  <div class="contact dark" style="right:10px;top:12px">42 Quenby Crescent<br>Kestrel Vale NSW 2188<br>brightharbourmakeovers@fernpost.example<br>ABN: 284 907 362</div>
  <div class="watermark" style="left:70px;top:105px" role="img" aria-label="Faint brand mark">
    <span class="watermark-ring" style="width:150px;height:150px"></span>
  </div>
  <svg class="band" style="bottom:0" viewBox="0 0 300 40" height="40" preserveAspectRatio="none">
    <path d="M0 40V30C120 34 200 6 300 8V40Z" fill="url(#swoosh)"/>
  </svg>
</section>

<!-- Letterhead, centred logo, front -->
<section class="sheet letterhead-b" aria-label="Letterhead, centred layout">
  <div class="brand" style="left:50%;top:10px;transform:translateX(-50%)"><span class="brand-dot" style="width:14px;height:14px"></span><span class="brand-name" style="font-size:8px">Bright Harbour Makeovers</span></div>
  <div class="watermark" style="left:70px;top:115px" role="img" aria-label="Faint brand mark">
    <span class="watermark-ring" style="width:150px;height:150px"></span>
  </div>
  <svg class="band" style="bottom:0" viewBox="0 0 293 46" height="46" preserveAspectRatio="none">
    <path d="M0 46V26C90 10 190 6 293 14V46Z" fill="url(#swoosh-rev)"/>
    <path d="M0 22C90 6 190 2 293 10" stroke="#1b1b1b" stroke-width="1" fill="none"/>
  </svg>
  <div class="contact" style="right:10px;bottom:8px">42 Quenby Crescent · Kestrel Vale NSW 2188<br>brightharbourmakeovers@fernpost.example · ABN: 284 907 362</div>
</section>

<!-- Business card front -->
<section class="sheet card-front" aria-label="Business card, Tessa Whitlock">
  <svg class="band" style="bottom:0" viewBox="0 0 151 18" height="18" preserveAspectRatio="none">
    <path d="M0 18V12C50 4 100 4 151 8V18Z" fill="url(#swoosh)"/>
  </svg>
  <div class="brand" style="left:5px;top:5px"><span class="brand-dot" style="width:8px;height:8px"></span><span class="brand-name" style="font-size:5px">Bright Harbour Makeovers</span></div>
  <div class="card-text" style="left:6px;top:18px"><strong>Tessa Whitlock</strong><br>Director</div>
</section>

<!-- Business card second name -->
<section class="sheet card-back" aria-label="Business card, Lewis Whitlock">
  <svg class="band" style="bottom:0" viewBox="0 0 144 18" height="18" preserveAspectRatio="none">
    <path d="M0 18V12C50 4 100 4 144 8V18Z" fill="url(#swoosh)"/>
  </svg>
  <div class="brand" style="left:5px;top:5px"><span class="brand-dot" style="width:8px;height:8px"></span><span class="brand-name" style="font-size:5px">Bright Harbour Makeovers</span></div>
  <div class="card-text" style="left:6px;top:18px"><strong>Lewis Whitlock</strong><br>Director</div>
</section>

<!-- Business card reverse, orange -->
<section class="sheet card-orange" aria-label="Business card reverse">
  <div class="watermark" style="left:0;top:0;width:100%;height:100%">
    <span class="watermark-ring" style="width:46px;height:46px;border-width:5px;border-color:rgba(255,255,255,.35)"></span>
  </div>
</section>

<!-- Envelope -->
<section class="sheet envelope" aria-label="Envelope">
  <svg class="band" style="top:0" viewBox="0 0 329 34" height="34" preserveAspectRatio="none">
    <rect width="329" height="30" fill="url(#flap)"/>
    <path d="M0 30C110 36 220 36 329 30" stroke="#e3791c" stroke-width="1.5" fill="none"/>
  </svg>
  <div class="brand" style="left:50%;top:9px;transform:translateX(-50%)"><span class="brand-dot" style="width:14px;height:14px;box-shadow:0 0 0 2px #fff"></span></div>
</section>

<!-- Compliment slip -->
<section class="sheet slip" aria-label="Compliment slip">
  <div class="brand" style="left:8px;top:10px"><span class="brand-dot" style="width:12px;height:12px"></span><span class="brand-name" style="font-size:7px">Bright Harbour Makeovers</span></div>
  <div class="watermark" style="left:225px;top:20px" role="img" aria-label="Faint brand mark">
    <span class="watermark-ring" style="width:95px;height:95px;border-width:8px"></span>
  </div>
  <svg class="band" style="bottom:0" viewBox="0 0 329 34" height="34" preserveAspectRatio="none">
    <path d="M0 34V22C110 10 220 8 329 14V34Z" fill="url(#swoosh)"/>
    <path d="M0 18C110 6 220 4 329 10" stroke="#1b1b1b" stroke-width=".8" fill="none"/>
  </svg>
</section>

</body>
</html>
```